Business card design for new eCommerce site focusing on integrity and strong businsess tactics

We need a business card that will stand out and be memorable. Something with color that matches our company logo colors. Think high end version of Tallyhop. There are 2 logos provided. The parent company is called Brightwell Craft Partners and we are presenting a new and very exciting eCommerce site called KestrelTradeHub.example.

Target Market(s)

Our target markets are in the Activities, Food and Beverage, Health and Beauty

Industry/Entity Type

Marketing

Contact Information for Business Card

We have 4 members that need cards...I will provide all info to the winner of the design contest
Business Address is
47390 West 63rd Lane, Suite K204
Phoenix AZ 85061

Font styles to use
Serif
Sans Serif

Colors

Designer to choose colors to be used in the design.

Requirements
Must have
• The card must be memorable...should be unique in design but must exude integrity and be playful .
• I have provided several colors or our parent company...please feel free to use which ever
Nice to have
• I will leave this up to you. Feel free to use other images of your choosing that wraps around our client.....Activities, Dining, Health, Beauty
Should not have
• just dont be boring

```html
<!DOCTYPE html>
<html lang="en">
<head>
<meta charset="utf-8">
<title>Brightwell Craft Partners – Business Card</title>
<link href="https://fonts.googleapis.com/css2?family=Montserrat:wght@600&family=Roboto:wght@400;700&display=swap" rel="stylesheet">
<style>
  :root {
    --backdrop: #a9a9a9;
    --lime: #8cb83a;
    --teal: #1e7878;
    --brand-teal: #2d918d;
    --card-white: #f3f3f1;
    --ink: #2b2b2b;
    --logo-light: #f2f4ee;
    --partner-green: #3d8a3a;
  }
  * { box-sizing: border-box; margin: 0; padding: 0; }
  html, body { width: 1200px; height: 576px; overflow: hidden; }
  body {
    background: var(--backdrop);
    position: relative;
    font-family: "Roboto", Arial, sans-serif;
  }
  .card {
    position: absolute;
    border-radius: 13px;
    overflow: hidden;
  }
  .card-front {
    left: 81px; top: 138px; width: 485px; height: 294px;
    background: linear-gradient(180deg, var(--lime) 0%, #7fb040 28%, #3a9470 62%, var(--teal) 100%);
  }
  .card-back {
    left: 602px; top: 138px; width: 480px; height: 291px;
    background: var(--card-white);
  }
  .faint-ring {
    position: absolute;
    border-radius: 50%;
    border: 18px solid rgba(255,255,255,0.08);
  }
  .card-front .faint-ring { left: 300px; top: 20px; width: 220px; height: 220px; }
  .card-back .faint-ring { left: 265px; top: 20px; width: 220px; height: 220px; border-color: rgba(0,0,0,0.04); }

  .front-mark {
    position: absolute; left: 183px; top: 62px; width: 120px; height: 120px;
    border-radius: 50%; background: #fff;
    box-shadow: 0 0 0 3px var(--lime), 0 0 0 4px rgba(255,255,255,0.8);
  }
  .front-name {
    position: absolute; left: 0; right: 0; top: 196px; text-align: center;
    font-family: "Montserrat", Arial, sans-serif; font-weight: 600;
    font-size: 27px; color: var(--logo-light);
  }

  .back-mark {
    position: absolute; left: 69px; top: 79px; width: 94px; height: 94px;
    border-radius: 50%; background: var(--brand-teal);
  }
  .back-name {
    position: absolute; left: 20px; width: 192px; top: 182px; text-align: center;
    font-family: "Montserrat", Arial, sans-serif; font-weight: 600;
    font-size: 19px; line-height: 21px; color: var(--brand-teal);
  }
  .divider {
    position: absolute; left: 221px; top: 66px; width: 1.5px; height: 160px;
    background: var(--lime);
  }
  .details { position: absolute; left: 252px; top: 66px; color: var(--ink); }
  .employee-name {
    font-weight: 700; font-size: 20px; color: var(--brand-teal); line-height: 24px;
  }
  .employee-title { font-size: 12px; margin-top: 4px; }
  .contact-list { list-style: none; margin-top: 22px; }
  .contact-list li {
    display: flex; align-items: center; gap: 8px;
    font-size: 13px; line-height: 18px;
  }
  .contact-list svg { width: 12px; height: 12px; fill: #555; flex: none; }
  .address { font-size: 13px; line-height: 17px; margin-top: 6px; }

  .partner {
    position: absolute; left: 19px; top: 250px;
    display: flex; align-items: center; gap: 6px;
    font-family: "Montserrat", Arial, sans-serif; font-weight: 600;
    font-size: 10px; color: var(--partner-green);
  }
  .partner-dot { width: 14px; height: 14px; border-radius: 50%; background: var(--lime); }
</style>
</head>
<body>
  <section class="card card-front">
    <div class="faint-ring"></div>
    <div class="front-mark"></div>
    <div class="front-name">Brightwell Craft Partners</div>
  </section>

  <section class="card card-back">
    <div class="faint-ring"></div>
    <div class="back-mark"></div>
    <div class="back-name">Brightwell Craft Partners</div>
    <div class="divider"></div>
    <div class="details">
      <div class="employee-name">Employee Name</div>
      <div class="employee-title">Managing Director</div>
      <ul class="contact-list">
        <li><svg viewBox="0 0 12 12"><path d="M1 3c0-1 1-2 2-2h6c1 0 2 1 2 2v1H8V3H4v1H1zM2 5h8l1 5H1z"/></svg>1800-555-0142</li>
        <li><svg viewBox="0 0 12 12"><path d="M0 2h12v8H0zM1 3l5 4 5-4v-.2H1z" fill-rule="evenodd"/></svg>name@kestreltradehub.example</li>
        <li><svg viewBox="0 0 12 12"><path d="M6 0a6 6 0 100 12A6 6 0 006 0zm0 1.2c.8.8 1.3 2.3 1.4 4.2H4.6C4.7 3.5 5.2 2 6 1.2zM4.6 6.6h2.8C7.3 8.5 6.8 10 6 10.8 5.2 10 4.7 8.5 4.6 6.6zM1.3 5.4A4.8 4.8 0 013.9 1.7c-.5 1-.9 2.3-.9 3.7zm0 1.2H3c0 1.4.4 2.7.9 3.7a4.8 4.8 0 01-2.6-3.7zm9.4 0A4.8 4.8 0 018.1 10.3c.5-1 .9-2.3.9-3.7zm0-1.2H9c0-1.4-.4-2.7-.9-3.7a4.8 4.8 0 012.6 3.7z"/></svg>www.kestreltradehub.example</li>
      </ul>
      <p class="address">47390 West 63rd Lane, Suite<br>K204, Phoenix AZ 85061</p>
    </div>
    <div class="partner"><span class="partner-dot"></span>VerdaPath.example</div>
  </section>
</body>
</html>
```